Heron Trade finance web design

We are a newly established business which provides invoice finance to Small Businesses in England and Wales.
Our approach is very much a funder where the small business owner can talk to the decision maker. We will guarantee on receipt of information, a decision within 24 hours.
We are not a bank so the look of the website need to be friendly but professional.
Have two types of people we are trying to attract to the website: 1) partners who are small business owners and 2) introducers who is accountants and commercial brokers who introduce us to the small businesses.
Currently no website, although domain has been reserved.
The design should be:
Professional
“Clean” Look
Designed to convey Trust and Authority.
Appeal to the small business owner.
Must incorporate:
Logo (attached)
Front page:Top tabs to other pages 1) About us 2) Services 3) Introducers 4) Contact us
Need picture and logo on page.
1) About us page- Room for talk about the company, the people and our critera.
2) Services page- We need for what invoice finance is, and 5 boxes for different services we will provide. (link on page to contact us)
3) Introducers page- We need a part for why become an introducer? Who we can help? Why we are different? (link on page to contact us)
4) Contact us page- Office address, email, tel and if possible a map and a contact me part which will email direct to us.
Text will be provided for the design, if we can see the setup of the website we will provide a part for each of the pages to support.
Styles we think convey the correct image:
www.brindlecapital.example
www.tollmarkfs.example
www.qelfunding.example
Small business owners
Finance
5+ page

```html
<!DOCTYPE html>
<html lang="en">
<head>
<meta charset="utf-8">
<title>Heron Trade Finance</title>
<link href="https://fonts.googleapis.com/css2?family=Open+Sans:ital,wght@0,400;0,600;1,400&family=Poiret+One&family=Cormorant+Garamond:ital,wght@1,400&display=swap" rel="stylesheet">
<style>
:root{
  --red:#e31e2a;
  --ink:#222;
  --text:#555;
  --muted:#888;
  --line:#e2e2e2;
  --band:#2b2b2b;
  --footer:#ececec;
  --num:#dcdcdc;
}
*{box-sizing:border-box;margin:0;padding:0}
html,body{width:1200px;height:2299px;overflow:hidden;background:#fff}
body{position:relative;font-family:"Open Sans",Arial,sans-serif;color:var(--text)}
.abs{position:absolute}
.thin{font-family:"Poiret One",Arial,sans-serif;color:var(--ink);font-weight:400}

/* header */
.brand{left:74px;top:28px;display:flex;align-items:center;gap:10px;color:var(--red);font-size:30px;font-weight:600;letter-spacing:-.3px}
.brand-dot{width:16px;height:16px;border-radius:50%;background:var(--red)}
.support{right:234px;top:32px;text-align:right;font-size:12px;line-height:18px;color:#333}
.phone-pill{left:980px;top:33px;width:146px;height:34px;border-radius:17px;background:var(--red);color:#fff;font-size:17px;display:flex;align-items:center;justify-content:center}

/* nav */
.nav{left:0;top:98px;width:1200px;height:37px;border-top:1px solid #ddd;border-bottom:1px solid #ddd;background:#f7f7f7}
.nav-list{position:absolute;left:74px;top:0;display:flex;height:35px;list-style:none}
.nav-list li{font-size:12px;color:#333;text-transform:uppercase;display:flex;align-items:center;padding:0 23px}
.nav-list li.active{background:var(--red);color:#fff;padding:0 30px}
.search{left:869px;top:0;width:257px;height:35px;background:#e3e3e3;display:flex;align-items:center;gap:8px;padding-left:12px;font-size:12px;color:#777}

/* hero */
.hero{left:0;top:135px;width:1200px;height:539px;background:linear-gradient(100deg,#4a3a22 0%,#7a6230 22%,#5b5346 45%,#3d4a60 62%,#6a6a70 80%,#8b8378 100%)}
.hero-copy{left:103px;top:142px;width:400px;color:#fff}
.hero-copy h1{font-size:23px;font-weight:400;line-height:32px}
.hero-copy p{margin-top:20px;font-size:16px;font-style:italic;line-height:26px}
.hero-btn{left:103px;top:356px;width:182px;height:37px;border-radius:19px;background:var(--red);color:#fff;font-size:16px;display:flex;align-items:center;justify-content:center}
.slide-arrow{top:245px;width:48px;height:48px;border:2px solid #fff;border-radius:50%;background:rgba(0,0,0,.35);display:flex;align-items:center;justify-content:center}

/* band */
.band{left:0;top:674px;width:1200px;height:92px;background:var(--band)}
.band p{position:absolute;left:72px;top:22px;width:730px;color:#fff;font-size:17px;line-height:24px}
.band-btn{left:855px;top:28px;width:228px;height:36px;border-radius:18px;background:var(--red);color:#fff;font-size:16px;display:flex;align-items:center;justify-content:center}

/* section heads */
.sec-title{left:0;width:1200px;text-align:center;font-size:30px;letter-spacing:.5px}
.sec-sub{left:0;width:1200px;text-align:center;font-size:15px;color:var(--text)}
.divider{left:74px;width:1053px;height:1px;background:var(--line)}

/* services */
.services{left:74px;top:930px;width:1053px;height:252px;display:flex}
.service{flex:1;border-left:1px solid var(--line);text-align:center;padding:0 14px}
.service:first-child{border-left:none}
.service svg{display:block;margin:6px auto 0}
.service h3{margin-top:26px;font-size:17px;font-weight:400;color:var(--ink)}
.service p{margin-top:10px;font-size:13px;line-height:20px;color:var(--text)}
.read-more{margin-top:18px;font-size:12px;color:var(--muted)}

/* about */
.about-photo{left:74px;top:1330px;width:538px;height:310px;background:linear-gradient(120deg,#3a3f48,#6f5a48 45%,#b59a80 70%,#4a4440)}
.about-photo::after{content:"";position:absolute;inset:10px 10px 10px 10px;border:2px solid #fff}
.about-copy{left:668px;top:1326px;width:460px}
.about-copy h2{font-size:30px;letter-spacing:.5px}
.about-copy p{margin-top:14px;font-size:13px;line-height:22px;color:var(--text)}
.about-copy .read-more{margin-top:20px}

/* why */
.why{left:74px;top:1880px;width:1053px;display:flex;gap:0}
.why-item{width:360px;display:flex;gap:18px}
.why-num{font-family:"Cormorant Garamond",Georgia,serif;font-style:italic;font-size:86px;line-height:80px;color:var(--num);width:84px;flex:none}
.why-item h3{font-size:18px;font-weight:400;color:var(--ink);margin-top:8px}
.why-item p{margin-top:10px;font-size:13px;line-height:20px;color:var(--text);width:230px}

/* footer */
.footer{left:0;top:2054px;width:1200px;height:245px;background:var(--footer)}
.f-title{position:absolute;font-size:18px;top:42px}
.f-col{position:absolute;top:84px;font-size:13px;line-height:21px;color:#555}
.f-vline{position:absolute;left:598px;top:40px;width:1px;height:125px;background:#d6d6d6}
.email-field{position:absolute;left:676px;top:92px;width:312px;height:46px;background:#fff;font-size:13px;color:#888;display:flex;align-items:center;padding-left:18px}
.subscribe{position:absolute;left:998px;top:92px;width:128px;height:46px;background:var(--red);color:#fff;font-size:13px;display:flex;align-items:center;justify-content:center;text-transform:uppercase}
.f-hline{position:absolute;left:74px;top:181px;width:1053px;height:1px;background:#d6d6d6}
.copyright{position:absolute;left:74px;top:205px;font-size:12px;color:#555}
.connect{position:absolute;left:800px;top:205px;font-size:12px;color:#555}
.socials{position:absolute;left:918px;top:194px;display:flex;gap:6px}
.socials span{width:37px;height:37px;background:#cfcfcf;display:block}
</style>
</head>
<body>

<header>
  <div class="abs brand"><span class="brand-dot"></span>Heron Trade Finance</div>
  <div class="abs support">Any Question? 24 hr Support<br>Call Us today!</div>
  <div class="abs phone-pill">1800 55 0142</div>
</header>

<nav class="abs nav">
  <ul class="nav-list">
    <li class="active">Home</li>
    <li>About Us</li>
    <li>Services</li>
    <li>Introducers</li>
    <li>Contact Us</li>
  </ul>
  <div class="abs search">
    <svg width="13" height="13" viewBox="0 0 13 13"><circle cx="5.5" cy="5.5" r="4.3" fill="none" stroke="#777" stroke-width="1.5"/><line x1="8.6" y1="8.6" x2="12" y2="12" stroke="#777" stroke-width="1.6"/></svg>
    Search
  </div>
</nav>

<section class="abs hero" role="img" aria-label="Smiling workshop worker in overalls leaning on a bench in a warehouse">
  <div class="abs hero-copy">
    <h1>Our approach is very much a funder where the small business owner can talk to the decision maker.</h1>
    <p>We will guarantee on receipt of information, a decision within 24 hours.</p>
  </div>
  <div class="abs hero-btn">Contact Us Today!</div>
  <div class="abs slide-arrow" style="left:12px"><svg width="16" height="16" viewBox="0 0 16 16"><polyline points="10,2 4,8 10,14" fill="none" stroke="#fff" stroke-width="2.4"/></svg></div>
  <div class="abs slide-arrow" style="left:1140px"><svg width="16" height="16" viewBox="0 0 16 16"><polyline points="6,2 12,8 6,14" fill="none" stroke="#fff" stroke-width="2.4"/></svg></div>
</section>

<section class="abs band">
  <p>Lorem Ipsum is simply dummy text of the printing and typesetting industry. Lorem Ipsum has been the industry's standard dummy text ever since the 1500s</p>
  <svg class="abs" style="left:775px;top:40px" width="75" height="34" viewBox="0 0 75 34"><path d="M3 14 Q30 40 68 20" fill="none" stroke="#aaa" stroke-width="1.6"/><polyline points="58,16 69,19 62,28" fill="none" stroke="#aaa" stroke-width="1.6"/></svg>
  <div class="abs band-btn">Become An Introducer</div>
</section>

<h2 class="abs thin sec-title" style="top:812px">SERVICES WE PROVIDE</h2>
<p class="abs sec-sub" style="top:862px">Lorem Ipsum has been the industry's standard dummy text ever since the 1500s.</p>

<section class="abs services">
  <div class="service">
    <svg width="90" height="86" viewBox="0 0 90 86" fill="none" stroke="#888" stroke-width="2"><polyline points="8,60 28,40 42,50 72,18"/><polyline points="60,18 72,18 72,30"/><circle cx="44" cy="66" r="14"/><path d="M44 58v16M48 61h-6a3 3 0 0 0 0 6h4a3 3 0 0 1 0 6h-6"/></svg>
    <h3>Service Title</h3>
    <p>Lorem Ipsum is simply dummy text standard dummy text ever has been the industry.</p>
    <div class="read-more">⊙ Read More</div>
  </div>
  <div class="service">
    <svg width="90" height="86" viewBox="0 0 90 86" fill="none" stroke="#888" stroke-width="2"><circle cx="45" cy="43" r="34"/><circle cx="45" cy="43" r="9"/><path d="M45 22v8M45 56v8M24 43h8M58 43h8M30 28l6 6M54 52l6 6M30 58l6-6M54 34l6-6"/></svg>
    <h3>Service Title</h3>
    <p>Lorem Ipsum is simply dummy text standard dummy text ever has been the industry.</p>
    <div class="read-more">⊙ Read More</div>
  </div>
  <div class="service">
    <svg width="90" height="86" viewBox="0 0 90 86" fill="none" stroke="#888" stroke-width="2"><circle cx="45" cy="45" r="30"/><path d="M45 15v30h30"/><path d="M49 41V19a26 26 0 0 1 22 22z" fill="#bbb" stroke="none"/></svg>
    <h3>Service Title</h3>
    <p>Lorem Ipsum is simply dummy text standard dummy text ever has been the industry.</p>
    <div class="read-more">⊙ Read More</div>
  </div>
  <div class="service">
    <svg width="90" height="86" viewBox="0 0 90 86" fill="none" stroke="#888" stroke-width="2"><rect x="26" y="8" width="54" height="38" rx="3"/><path d="M12 26h50v36H34l-12 12v-12H12z" fill="#fff"/><path d="M20 38h34M20 46h34M20 54h24"/></svg>
    <h3>Service Title</h3>
    <p>Lorem Ipsum is simply dummy text standard dummy text ever has been the industry.</p>
    <div class="read-more">⊙ Read More</div>
  </div>
  <div class="service">
    <svg width="90" height="86" viewBox="0 0 90 86" fill="none" stroke="#888" stroke-width="2"><path d="M40 8h10l2 10 8 4 9-6 7 7-6 9 4 8 10 2v10l-10 2-4 8 6 9-7 7-9-6-8 4-2 10H40l-2-10-8-4-9 6-7-7 6-9-4-8-10-2V38l10-2 4-8-6-9 7-7 9 6 8-4z"/><circle cx="45" cy="43" r="12"/></svg>
    <h3>Service Title</h3>
    <p>Lorem Ipsum is simply dummy text standard dummy text ever has been the industry.</p>
    <div class="read-more">⊙ Read More</div>
  </div>
</section>

<div class="abs divider" style="top:1256px"></div>

<section>
  <div class="abs about-photo" role="img" aria-label="Team of colleagues in discussion around a meeting table"></div>
  <div class="abs about-copy">
    <h2 class="thin">ABOUT OUR COMPANY</h2>
    <p>Lorem Ipsum is simply dummy text of the printing and typesetting industry. Lorem Ipsum has been the industry's standard dummy text ever since the 1500s, when an unknown printer took a galley of type and scrambled it to make a type specimen book.</p>
    <p>It was popularised in the 1960s with the release of Letraset sheets containing Lorem Ipsum passages, and more recently with desktop publishing software like Aldus PageMaker including versions of Lorem Ipsum.</p>
    <div class="read-more">⊙ More Information About Company</div>
  </div>
</section>

<div class="abs divider" style="top:1713px"></div>

<h2 class="abs thin sec-title" style="top:1778px">WHY WE ARE DIFFERENT?</h2>
<p class="abs sec-sub" style="top:1828px">Lorem Ipsum has been the industry's standard dummy text ever since the 1500s.</p>

<section class="abs why">
  <div class="why-item"><div class="why-num">01</div><div><h3>Over 50 years of experience</h3><p>Lorem Ipsum has been the industry's took a galley of type it to make a type specimen book.</p></div></div>
  <div class="why-item"><div class="why-num">02</div><div><h3>We fast, accuracy &amp; reliable</h3><p>Lorem Ipsum has been the industry's took a galley of type it to make a type specimen book.</p></div></div>
  <div class="why-item"><div class="why-num">03</div><div><h3>We are improving everyday</h3><p>Lorem Ipsum has been the industry's took a galley of type it to make a type specimen book.</p></div></div>
</section>

<footer class="abs footer">
  <h4 class="thin f-title" style="left:74px">GET IN TOUCH</h4>
  <div class="f-col" style="left:74px">Heron Trade Finance Limited<br>228, Lorem ipsum dolor,<br>Dosis anet - 84589</div>
  <div class="f-col" style="left:345px">T: 1800 55 0142<br>E: info@herontrade.example</div>
  <div class="f-vline"></div>
  <h4 class="thin f-title" style="left:676px">SUBSCRIBE OUR NEWSLETTER</h4>
  <div class="email-field">Email Address</div>
  <div class="subscribe">Subscribe</div>
  <div class="f-hline"></div>
  <div class="copyright">Copyright © 2016 Heron Trade Finance Limited. All Rights Reserved</div>
  <div class="connect">Connect With Us :</div>
  <div class="socials"><span></span><span></span><span></span><span></span><span></span></div>
</footer>

</body>
</html>
```